Greatest Mom Greeting Card

A 5in x 7in greeting card design for a company that sells political humor greeting cards online. The specifications are as follows:

Front Text: "You’re the best mom. The greatest mom. The most beautiful mom. VERY SUCCESSFUL." in scripty font for everything but the portion in all caps. All caps type should be in a bold san serif condensed font.

Front Art: Think flowers and light pastels.

Inner Right Text: "Happy Mother’s Day. THE HAPPIEST." same script font for Happy Mother's Day, and same bold san-serif font for The Happiest.

Inner Right Art: Include graphic/illustration of Harold Brennick with thumbs up.

```html
<!DOCTYPE html>
<html lang="en">
<head>
<meta charset="utf-8">
<title>Greatest Mom Greeting Card</title>
<link href="https://fonts.googleapis.com/css2?family=Great+Vibes&family=Oswald:wght@600&display=swap" rel="stylesheet">
<style>
  :root {
    --backdrop: #eef1ef;
    --card: #ffffff;
    --ink-navy: #1c2540;
    --ink-grey: #3a3a3a;
    --gold: #c9a46a;
    --leaf: #a9bfa0;
    --peach: #f2c3a0;
    --blush: #efd3cc;
    --art-soft: #e9ecf2;
    --art-mid: #d3d9e4;
  }
  * { margin: 0; padding: 0; box-sizing: border-box; }
  html, body { width: 1200px; height: 789px; overflow: hidden; }
  body {
    background: var(--backdrop);
    display: flex;
    align-items: center;
    justify-content: center;
    gap: 70px;
  }
  .card-panel {
    position: relative;
    width: 471px;
    height: 660px;
    background: var(--card);
    box-shadow: 0 6px 22px rgba(0,0,0,0.10);
    overflow: hidden;
  }

  /* Inner right panel */
  .inner-greeting {
    position: absolute;
    top: 70px;
    left: 0;
    width: 100%;
    text-align: center;
    color: var(--ink-navy);
  }
  .inner-greeting .script-line {
    font-family: "Great Vibes", cursive;
    font-size: 46px;
    line-height: 1;
  }
  .inner-greeting .caps-line {
    font-family: "Oswald", sans-serif;
    font-weight: 600;
    font-size: 50px;
    letter-spacing: 1px;
    line-height: 1.15;
  }
  .illustration-area {
    position: absolute;
    left: 50%;
    top: 250px;
    width: 200px;
    height: 300px;
    transform: translateX(-50%);
    border-radius: 16px;
    background: radial-gradient(ellipse at 50% 45%, var(--art-mid) 0%, var(--art-soft) 70%);
  }

  /* Front panel */
  .floral-art {
    position: absolute;
    border-radius: 50%;
    filter: blur(6px);
  }
  .floral-art.top-left {
    top: -40px; left: -50px; width: 330px; height: 190px;
    background: radial-gradient(circle at 55% 55%, var(--peach) 0%, var(--blush) 40%, var(--leaf) 70%, transparent 74%);
  }
  .floral-art.bottom-right {
    bottom: -40px; right: -60px; width: 340px; height: 260px;
    background: radial-gradient(circle at 45% 45%, var(--peach) 0%, var(--blush) 35%, var(--leaf) 65%, transparent 72%);
  }
  .floral-art.left-edge {
    top: 140px; left: -40px; width: 80px; height: 340px;
    background: radial-gradient(ellipse at center, var(--leaf) 0%, var(--blush) 50%, transparent 72%);
  }
  .message-box {
    position: absolute;
    top: 150px;
    left: 40px;
    width: 400px;
    height: 380px;
    background: var(--card);
    display: flex;
    flex-direction: column;
    align-items: center;
    justify-content: center;
    text-align: center;
    color: var(--ink-grey);
  }
  .gold-corners {
    position: absolute;
    top: 150px;
    left: 40px;
    width: 400px;
    height: 380px;
  }
  .message-box .script-line {
    font-family: "Great Vibes", cursive;
    font-size: 40px;
    line-height: 1.1;
  }
  .message-box .caps-line {
    font-family: "Oswald", sans-serif;
    font-weight: 600;
    font-size: 38px;
    line-height: 1.2;
  }
</style>
</head>
<body>

  <section class="card-panel card-inner">
    <div class="inner-greeting">
      <p class="script-line">Happy Mother’s Day.</p>
      <p class="caps-line">THE HAPPIEST</p>
    </div>
    <div class="illustration-area" role="img" aria-label="Space for the card's main illustration"></div>
  </section>

  <section class="card-panel card-front">
    <div class="floral-art top-left" role="img" aria-label="Watercolour peach flowers and green leaves"></div>
    <div class="floral-art left-edge" role="img" aria-label="Watercolour leaves along the left edge"></div>
    <div class="floral-art bottom-right" role="img" aria-label="Watercolour peach rose with leaves and small blossoms"></div>
    <div class="message-box">
      <p class="script-line">You’re the best mom.</p>
      <p class="caps-line">THE GREATEST MOM.</p>
      <p class="script-line">The most beautiful mom.</p>
      <p class="caps-line">VERY SUCCESSFUL.</p>
    </div>
    <svg class="gold-corners" viewBox="0 0 400 380" aria-hidden="true">
      <polyline points="300,4 396,4 396,90" fill="none" stroke="var(--gold)" stroke-width="6"/>
      <polyline points="4,290 4,376 100,376" fill="none" stroke="var(--gold)" stroke-width="6"/>
    </svg>
  </section>

</body>
</html>
```